Signage Design Project

An advertising display panel for our vending machine. The display should look stylish (these machines will be located in a bar), however it should also inform as to what the product is... most people will not have seen this product and will not know what it is.

I have attached:
1. photo of the machine (I do not have the exact dimensions of the advertising display panel, but the machine dimensions are 1600 x 478 x 415mm)
2. mock ups of ideas I have been toying with but that I am not content with
3. low resolution versions of the image I would like to use to communicate what the product is and does (please note there are other colours we use being black, raspberry, silver, green... I send email these on request)

Target Market(s)

18 to 40 year old males and females in bars and clubs

Industry/Entity Type

Advertising

Requirements
Must have
• Stylish
Photo of our product connected to an Zorbex

```html
<!DOCTYPE html>
<html lang="en">
<head>
<meta charset="utf-8">
<title>Voltlet – Display Panel</title>
<link rel="stylesheet" href="https://fonts.googleapis.com/css2?family=Comfortaa:wght@400;500&display=swap">
<style>
  :root {
    --backdrop: #8a8a8a;
    --panel: #ffffff;
    --brand-grey: #6f6f6f;
    --accent-orange: #ef9a2a;
    --body-grey: #7a7a7a;
    --product-teal: #3cc3dc;
    --product-teal-soft: #bfe9f2;
    --photo-light: #f5f7f8;
    --photo-dark: #4a4d50;
  }
  html, body {
    margin: 0;
    padding: 0;
    width: 799px;
    height: 1200px;
    overflow: hidden;
    background: var(--backdrop);
  }
  .display-panel {
    position: absolute;
    left: 199px;
    top: 134px;
    width: 402px;
    height: 945px;
    background: var(--panel);
    font-family: "Comfortaa", sans-serif;
  }
  .brand-name {
    position: absolute;
    left: 28px;
    top: 40px;
    margin: 0;
    font-size: 66px;
    font-weight: 400;
    letter-spacing: -1px;
    color: var(--brand-grey);
    line-height: 1;
  }
  .tagline {
    margin: 0;
    color: var(--accent-orange);
    font-weight: 500;
    line-height: 1;
  }
  .tagline span {
    position: absolute;
    white-space: nowrap;
  }
  .tagline-lead { left: 28px; top: 130px; font-size: 30px; }
  .tagline-where { left: 133px; top: 170px; font-size: 38px; }
  .tagline-when { left: 28px; top: 212px; font-size: 38px; }
  .product-shot {
    position: absolute;
    left: 36px;
    top: 262px;
    width: 310px;
    height: 150px;
    border-radius: 75px;
    background: linear-gradient(170deg, var(--photo-light) 0%, var(--product-teal-soft) 25%, var(--product-teal) 55%, var(--product-teal-soft) 85%, var(--photo-light) 100%);
  }
  .product-summary {
    position: absolute;
    left: 0;
    top: 452px;
    width: 100%;
    margin: 0;
    text-align: center;
    font-size: 21px;
    line-height: 30px;
    color: var(--body-grey);
  }
  .usage-shot {
    position: absolute;
    left: 62px;
    top: 562px;
    width: 250px;
    height: 345px;
    border-radius: 24px;
    background: linear-gradient(155deg, var(--photo-light) 0%, var(--photo-dark) 18%, var(--photo-dark) 38%, var(--product-teal-soft) 52%, var(--product-teal) 62%, var(--photo-light) 82%, var(--photo-light) 100%);
    opacity: 0.85;
  }
</style>
</head>
<body>
  <main class="display-panel">
    <h1 class="brand-name">voltlet</h1>
    <p class="tagline">
      <span class="tagline-lead">Recharge your device</span>
      <span class="tagline-where">anywhere</span>
      <span class="tagline-when">anytime</span>
    </p>
    <div class="product-shot" role="img" aria-label="Teal aluminium cylindrical portable charger lying at an angle"></div>
    <p class="product-summary">Portable battery driven chargers<br>for your phone, tablet, mp3,<br>camera, game and more...</p>
    <div class="usage-shot" role="img" aria-label="Teal portable charger connected by a white cable to a Zorbex smartphone, with three spare connector tips"></div>
  </main>
</body>
</html>
```